Need UI design for an iOS app game with most of the layout planned

The name of the game is "QUADRIX".

The goal of the game is to find a way to manipulate four numbers so that the end result is 24. Addition, subtraction, multiplication and division may be used and each number can only be used once.

The list of items we need is:

1. launch image, app icon, UI design of all scenes (10-12 scenes) of the app.
2. App background image should support screen size of both 640x1136.
3. Files are preferred to be in (.eps) format so that resolution can be adjusted later. But other file formats are welcome as long as resolution is high enough.
4. Icons, buttons, background image etc. should have their own file so that later they can be moved around in case design is changed.

The detailed requirement is in the attached file. The actual layout can vary if it can help achieve better result. We also attached several screenshots from iOS game "Glimbo". You can use that as your reference.

```html
<!DOCTYPE html>
<html lang="en">
<head>
<meta charset="utf-8">
<title>QUADRIX – Pause and Play Screens</title>
<link rel="stylesheet" href="https://fonts.googleapis.com/css2?family=Aleo:wght@300;400;700&family=Lato:wght@400;700&display=swap">
<style>
  :root {
    --canvas: #d3d4d6;
    --panel: #ffffff;
    --panel-gray: #f2f2f2;
    --ink: #231f20;
    --muted: #6d6e71;
    --accent-blue: #29a8e0;
    --accent-red: #f15a29;
    --play-green: #2bb673;
    --strip-dark: #3d3d3f;
    --star-dark: #3d3d44;
    --tile-yellow: #f6eb30;
    --tile-orange: #fbb040;
    --tile-purple: #a7679a;
    --tile-blue: #4a90cc;
    --tile-red: #ef4136;
    --key-green: #27b574;
    --key-lime: #8dc63f;
    --line: #d9d9d9;
  }
  * { box-sizing: border-box; margin: 0; padding: 0; }
  html, body { width: 1200px; height: 675px; overflow: hidden; background: var(--canvas); }
  .stage { position: absolute; left: 0; top: 0; width: 1366px; height: 768px; transform: scale(0.87848); transform-origin: 0 0; }
  .screen { position: absolute; width: 317px; height: 569px; background: var(--panel); overflow: hidden; font-family: "Aleo", Georgia, serif; color: var(--ink); }
  .screen--paused { left: 124px; top: 87px; }
  .screen--play { left: 566px; top: 90px; }
  .abs { position: absolute; }

  .header { position: absolute; left: 0; top: 0; width: 317px; height: 68px; background: var(--panel); }
  .level-title { position: absolute; left: 62px; width: 200px; top: 14px; text-align: center; font-weight: 700; font-size: 14px; }
  .progress { position: absolute; left: 91px; top: 35px; width: 144px; height: 8px; border: 1px solid var(--accent-blue); border-radius: 4px; overflow: hidden; }
  .progress__fill { width: 50%; height: 100%; background: var(--accent-blue); }
  .stars { position: absolute; left: 121px; top: 46px; }
  .coin { position: absolute; left: 275px; top: 20px; }
  .coin-count { position: absolute; left: 270px; width: 38px; top: 50px; text-align: center; font-family: "Lato", Arial, sans-serif; font-weight: 700; font-size: 13px; color: var(--muted); }

  .pause-title-band { top: 68px; height: 72px; width: 317px; background: var(--panel-gray); display: flex; align-items: center; justify-content: center; padding-top: 26px; font-weight: 300; font-size: 22px; letter-spacing: .5px; }
  .resume-band { top: 140px; height: 80px; width: 317px; background: var(--play-green); }
  .controls-band { top: 220px; height: 93px; width: 317px; background: var(--panel); }
  .help-band { top: 313px; height: 87px; width: 317px; background: var(--panel-gray); border-top: 0; }
  .help-band::before { content: ""; position: absolute; left: 0; right: 0; top: 21px; height: 1px; background: var(--line); }
  .help-title { position: absolute; top: 47px; width: 100%; text-align: center; font-weight: 300; font-size: 20px; }
  .helper-strip { top: 400px; height: 79px; width: 317px; background: var(--strip-dark); }
  .helper { position: absolute; top: 3px; width: 72px; height: 73px; display: flex; align-items: center; justify-content: center; }
  .helper--yellow { left: 5px; background: var(--tile-yellow); }
  .helper--orange { left: 83px; background: var(--tile-orange); }
  .helper--purple { left: 161px; background: var(--tile-purple); }
  .helper--blue { left: 239px; background: var(--tile-blue); }

  .fade { height: 45px; width: 317px; background: linear-gradient(#f2f2f2, #ffffff); }
  .footer { left: 0; width: 317px; height: 45px; border-top: 1px solid var(--line); background: var(--panel); }
  .pill { position: absolute; top: 13px; width: 98px; height: 23px; border: 1px solid var(--muted); border-radius: 12px; background: var(--panel); font-weight: 300; font-size: 13px; text-align: center; line-height: 21px; color: var(--ink); }
  .pill--muted { background: #e6e7e8; }

  .board { top: 68px; width: 317px; height: 426px; background: var(--panel-gray); }
  .board::after { content: ""; position: absolute; left: 0; right: 0; bottom: 0; height: 40px; background: linear-gradient(#f2f2f2, #ffffff); }
  .tile { position: absolute; width: 82px; height: 82px; border-radius: 6px; display: flex; align-items: center; justify-content: center; font-family: "Lato", Arial, sans-serif; font-size: 40px; color: #111; background: var(--tile-orange); }
  .tile--yellow { background: var(--tile-yellow); }
  .tile--red { background: var(--tile-red); }
  .key { position: absolute; top: 460px; width: 40px; height: 40px; border-radius: 3px; z-index: 1; display: flex; align-items: center; justify-content: center; }
  .key--green { background: var(--key-green); }
  .key--lime { background: var(--key-lime); }
  .key__label { font-family: "Lato", Arial, sans-serif; font-weight: 700; font-size: 28px; color: #fff; }
</style>
</head>
<body>
<svg width="0" height="0" style="position:absolute">
  <defs>
    <symbol id="star-shape" viewBox="0 0 24 24"><path d="M12 1.5l3.1 6.9 7.4.7-5.6 5 1.7 7.4L12 17.6 5.4 21.5l1.7-7.4-5.6-5 7.4-.7z"/></symbol>
  </defs>
</svg>

<main class="stage">
  <!-- Paused screen -->
  <section class="screen screen--paused" aria-label="Game paused">
    <header class="header">
      <div class="level-title">Level 01</div>
      <div class="progress"><div class="progress__fill"></div></div>
      <svg class="stars" width="80" height="20" viewBox="0 0 80 20">
        <use href="#star-shape" x="0" y="0" width="20" height="20" fill="var(--accent-red)"/>
        <use href="#star-shape" x="29" y="0" width="20" height="20" fill="none" stroke="var(--accent-red)" stroke-width="1.4"/>
        <use href="#star-shape" x="57" y="0" width="20" height="20" fill="none" stroke="var(--accent-red)" stroke-width="1.4"/>
      </svg>
      <svg class="coin" width="28" height="28" viewBox="0 0 28 28"><circle cx="14" cy="14" r="12.5" fill="none" stroke="var(--accent-blue)" stroke-width="2"/><text x="14" y="19" text-anchor="middle" font-family="Lato, sans-serif" font-size="14" fill="var(--accent-blue)">$</text></svg>
      <div class="coin-count">12</div>
    </header>

    <div class="abs pause-title-band">GAME PAUSED !</div>
    <div class="abs resume-band">
      <svg class="abs" style="left:140px;top:15px" width="44" height="50" viewBox="0 0 44 50"><path d="M0 0L44 25 0 50z" fill="#fff"/></svg>
    </div>
    <div class="abs controls-band">
      <svg class="abs" style="left:20px;top:20px" width="50" height="50" viewBox="0 0 50 50"><circle cx="25" cy="24" r="22" fill="none" stroke="var(--accent-blue)" stroke-width="3"/><path d="M18 17l14 14M32 17L18 31" stroke="var(--accent-blue)" stroke-width="3"/></svg>
      <svg class="abs" style="left:93px;top:17px" width="52" height="54" viewBox="0 0 52 54"><path d="M44 32A20 20 0 1 1 38 10" fill="none" stroke="var(--accent-blue)" stroke-width="3"/><path d="M16 12L42 27 16 42z" fill="var(--accent-blue)"/><path d="M18 46l7 6 2-8" fill="none" stroke="var(--accent-blue)" stroke-width="2.5"/></svg>
      <svg class="abs" style="left:172px;top:102px;top:23px" width="36" height="52" viewBox="0 0 36 52"><rect x="0" y="16" width="8" height="19" fill="var(--muted)"/><path d="M9 16L35 0V52L9 35z" fill="var(--muted)"/></svg>
      <svg class="abs" style="left:218px;top:37px" width="80" height="27" viewBox="0 0 80 27"><rect x="1" y="1" width="78" height="25" fill="#fff" stroke="var(--muted)" stroke-width="2"/><rect x="37" y="3" width="40" height="21" fill="var(--accent-blue)"/></svg>
    </div>
    <div class="abs help-band"><div class="help-title">Ask for Help</div></div>
    <div class="abs helper-strip">
      <div class="helper helper--yellow"><svg width="34" height="34"><use href="#star-shape" width="34" height="34" fill="var(--star-dark)" stroke="#fff" stroke-width=".6"/></svg></div>
      <div class="helper helper--orange"><svg width="34" height="34"><use href="#star-shape" width="34" height="34" fill="var(--star-dark)" stroke="#fff" stroke-width=".6"/></svg></div>
      <div class="helper helper--purple"><svg width="34" height="34"><use href="#star-shape" width="34" height="34" fill="var(--star-dark)" stroke="#fff" stroke-width=".6"/></svg></div>
      <div class="helper helper--blue"><svg width="34" height="34"><use href="#star-shape" width="34" height="34" fill="var(--star-dark)" stroke="#fff" stroke-width=".6"/></svg></div>
    </div>
    <div class="abs fade" style="top:479px"></div>
    <footer class="abs footer" style="top:524px">
      <div class="pill" style="left:42px;top:12px">Reset</div>
      <div class="pill pill--muted" style="left:169px;top:12px">Skip</div>
    </footer>
  </section>

  <!-- Play screen -->
  <section class="screen screen--play" aria-label="Level in play">
    <header class="header">
      <svg class="abs" style="left:4px;top:20px" width="28" height="28" viewBox="0 0 28 28"><circle cx="14" cy="14" r="12.5" fill="none" stroke="var(--accent-blue)" stroke-width="2"/><path d="M11 9v10M17 9v10" stroke="var(--accent-blue)" stroke-width="2"/></svg>
      <div class="level-title">Level 01</div>
      <div class="progress"><div class="progress__fill"></div></div>
      <svg class="stars" width="80" height="20" viewBox="0 0 80 20">
        <use href="#star-shape" x="0" y="0" width="20" height="20" fill="var(--accent-red)"/>
        <use href="#star-shape" x="29" y="0" width="20" height="20" fill="none" stroke="var(--accent-red)" stroke-width="1.4"/>
        <use href="#star-shape" x="57" y="0" width="20" height="20" fill="none" stroke="var(--accent-red)" stroke-width="1.4"/>
      </svg>
      <svg class="coin" width="28" height="28" viewBox="0 0 28 28"><circle cx="14" cy="14" r="12.5" fill="none" stroke="var(--accent-blue)" stroke-width="2"/><text x="14" y="19" text-anchor="middle" font-family="Lato, sans-serif" font-size="14" fill="var(--accent-blue)">$</text></svg>
      <div class="coin-count">12</div>
    </header>

    <div class="abs board">
      <div class="tile" style="left:76px;top:30px">1</div>
      <div class="tile" style="left:164px;top:30px">+</div>
      <div class="tile" style="left:76px;top:117px">2</div>
      <div class="tile tile--red" style="left:164px;top:117px">−</div>
      <div class="tile" style="left:76px;top:203px">3</div>
      <div class="tile" style="left:164px;top:203px">÷</div>
      <div class="tile tile--yellow" style="left:76px;top:289px">4</div>
      <div class="tile" style="left:164px;top:289px">×</div>
    </div>
    <div class="key key--green" style="left:51px"><svg width="26" height="26" viewBox="0 0 26 26"><path d="M4 4l18 18M22 4L4 22" stroke="#fff" stroke-width="5"/></svg></div>
    <div class="key key--lime" style="left:138px"><svg width="28" height="22" viewBox="0 0 28 22"><rect x="0" y="2" width="28" height="6" rx="1" fill="#fff"/><rect x="0" y="14" width="28" height="6" rx="1" fill="#fff"/></svg></div>
    <div class="key key--green" style="left:226px"><span class="key__label">?</span></div>

    <footer class="abs footer" style="top:524px">
      <div class="pill" style="left:42px">Reset</div>
      <div class="pill pill--muted" style="left:169px">Skip</div>
    </footer>
  </section>
</main>
</body>
</html>
```